Crate Up! Flyer Design - Double Sided, Get Creative!

We are looking for a flexible flyer design, DL sized print.

We are launching a new service - Crate Up! - which is basically a personal, urban self storage solution. We deliver boxes, our customer pack them, we collect and store and can re-deliver on demand.

For colour, logo and a better idea of the service please see our website www.simplycrateup.com.au

One side of the flyer will need a picture of the box, explanation of the service, a call to action with an offer, as well as a price. The tag line is Simply Crate UP!

The other side is where we need creative input. We are looking for something clean and modern, that appeals to a market 18 - 45. I am happy to explore the idea of multiple different concepts to target each market (ie. one targeting mothers, one targeting students, etc) and will pay for each of those if the concept is good.

Our target market is apartment dwellers, students, mothers with young children (but who have outgrown toys, etc), older people whose kids have left home, and people moving to smaller houses from larger ones.

The value proposition of our service is that:

1, Very cost effective
2 .Very convenient (delivered to/from your door)
3. No wasted space, so not wasting money

Please take inspiration from our website for font and colours.

Hi All,Just wanted to add that we are also going to need other collateral once this is done - posters, etc. So please think of this as more than just a one off job! Added Tuesday, February 24, 2015

Target Market(s)

People looking for storage of items / stuff. Our target market is apartment dwellers, students, mothers with young children (but who have outgrown toys, etc), older people whose kids have left home, and people moving to smaller houses from larger ones.

Industry/Entity Type

Self Storage

Font styles to use
Sans Serif

Requirements
Must have
• Our logo, a picture of our box, our value propositions, how the service works, call to action / offer.
• Side 1: Communicate the Idea of storage, mess - tidy. Maybe a cover to target each market vertical.
• Side 2: Picture of our box, our value propositions, how the service works, call to action / offer.
Nice to have
• Idea of mess -> tidy, etc.

```html
<!DOCTYPE html>
<html lang="en">
<head>
<meta charset="utf-8">
<title>Crate Up! Flyer</title>
<link href="https://fonts.googleapis.com/css2?family=PT+Sans:ital,wght@0,400;0,700;1,700&family=Open+Sans:ital,wght@0,600;1,600&family=Oswald:wght@500&family=Great+Vibes&family=Tinos&display=swap" rel="stylesheet">
<style>
:root{
  --page:#3d3e40;
  --sky-top:#7fd0f0;
  --sky-mid:#e6f5fb;
  --grass:#c9e4a8;
  --brand:#2a9fd6;
  --brand-dark:#236f8e;
  --teal:#2b6175;
  --navy:#10202e;
  --white:#ffffff;
  --ink:#1a1a1a;
  --paint:#f6a11c;
  --card-blue:#5cc9ef;
}
*{margin:0;padding:0;box-sizing:border-box}
html,body{width:1200px;height:1139px;overflow:hidden;background:var(--page);font-family:"PT Sans",sans-serif;color:var(--ink)}
.flyer{position:absolute;left:54px;width:1084px;height:511px;overflow:hidden}
.front{top:40px;background:linear-gradient(180deg,var(--sky-top) 0%,var(--sky-mid) 35%,#f2f8f4 60%,var(--grass) 82%)}
.back{top:574px;background:linear-gradient(180deg,var(--sky-top) 0%,var(--sky-mid) 30%,#f6fafc 70%)}
.abs{position:absolute}
.band-dark{position:absolute;left:0;width:100%;height:24px;background:var(--teal)}
.band-blue{position:absolute;left:0;width:100%;background:var(--brand);border-top:4px solid var(--white)}
.brand-name{position:absolute;display:flex;align-items:center;gap:14px;font-family:"PT Sans",sans-serif;font-weight:700;color:var(--brand);white-space:nowrap}
.brand-name .mark{display:block;background:var(--brand)}
.tagline{font-weight:700;font-style:italic;font-size:24px;color:var(--ink)}
.photo{position:absolute;border-radius:6px}
.offer-diamond{position:absolute;left:360px;top:246px;width:372px;height:372px}
.offer-text{position:absolute;left:360px;width:372px;text-align:center;color:var(--white)}
.offer-title{top:290px;font-family:"Open Sans",sans-serif;font-weight:600;font-size:38px}
.offer-from{top:360px;font-family:"Great Vibes",cursive;font-size:34px}
.offer-price{top:400px;font-weight:700;font-size:42px}
.offer-unit{top:448px;font-size:22px}
.offer-rule{position:absolute;left:470px;width:152px;height:2px;background:var(--white)}
.services-title{position:absolute;left:736px;top:72px;font-family:"Oswald",sans-serif;font-weight:500;font-size:36px;color:var(--navy);letter-spacing:-.5px}
.services{position:absolute;left:714px;top:174px;width:370px;list-style:none;font-size:15.6px;line-height:19.5px}
.services li{position:relative;padding-left:27px;margin-bottom:0}
.services li::before{content:"";position:absolute;left:2px;top:5px;width:9px;height:9px;background:var(--brand);transform:rotate(45deg)}
.contact-phone{position:absolute;font-weight:700;font-size:25px;color:var(--navy)}
.contact-mail{position:absolute;font-size:15px;color:var(--navy)}
.web{position:absolute;font-weight:700;font-size:31px;color:var(--navy)}
.how-title{position:absolute;left:342px;top:40px;width:252px;text-align:center;font-style:italic;font-weight:700;font-size:21px;color:var(--ink)}
.steps{position:absolute;left:336px;top:78px;width:252px}
.step{height:68px;margin-bottom:6px;padding-top:5px;text-align:center;color:var(--white);border-bottom:3px solid rgba(255,255,255,.5)}
.step:nth-child(odd){background:var(--brand)}
.step:nth-child(even){background:var(--teal)}
.step h3{font-size:20px;font-weight:700;line-height:22px}
.step p{font-size:14.5px;line-height:17px}
.store-card{position:absolute;left:686px;top:150px;width:390px;height:246px;background:var(--card-blue);border:4px solid var(--white);border-radius:12px;transform:rotate(6deg);box-shadow:0 4px 10px rgba(0,0,0,.25);padding:20px 22px}
.store-card h2{font-family:"Open Sans",sans-serif;font-style:italic;font-weight:600;font-size:27px;text-align:center;color:var(--ink);margin-bottom:12px}
.store-card p{font-family:"Tinos",serif;font-size:16.5px;line-height:19px;text-align:justify;color:var(--ink)}
.address{position:absolute;left:438px;top:446px;font-size:18px;color:var(--navy)}
</style>
</head>
<body>

<section class="flyer front">
  <div class="brand-name" style="left:40px;top:26px;font-size:78px"><span class="mark" style="width:58px;height:58px"></span>Crate Up!</div>
  <p class="abs tagline" style="left:48px;top:126px">Safe, secure and insured storage</p>
  <div class="photo" role="img" aria-label="Two open blue storage crates filled with folded clothes and a teddy bear" style="left:24px;top:166px;width:216px;height:202px;background:linear-gradient(160deg,#c97b8c,#2f8fd0 45%,#1f76b8)"></div>
  <div class="photo" role="img" aria-label="Delivery man in uniform leaning on a hand trolley stacked with cardboard boxes" style="left:426px;top:2px;width:180px;height:198px;background:linear-gradient(180deg,#c9d7e0,#8a8f94 55%,#c79a66)"></div>

  <div class="band-dark" style="top:382px"></div>
  <div class="band-blue" style="top:402px;height:109px"></div>

  <svg class="offer-diamond" viewBox="0 0 372 372" aria-hidden="true">
    <polygon points="186,0 372,186 186,372 0,186" fill="#5bb7e6"/>
    <polygon points="186,12 360,186 186,360 12,186" fill="#2a7fc6"/>
  </svg>
  <p class="offer-text offer-title">Offer</p>
  <span class="offer-rule" style="top:344px"></span>
  <p class="offer-text offer-from">From</p>
  <p class="offer-text offer-price">$5. 95</p>
  <p class="offer-text offer-unit">PER BOX PER MONTH</p>
  <span class="offer-rule" style="top:484px"></span>

  <div class="abs" role="img" aria-label="Orange paint splash with a paint roller" style="left:708px;top:32px;width:356px;height:126px;background:linear-gradient(90deg,var(--paint) 0%,#f8b33b 52%,rgba(246,161,28,0) 54%,rgba(0,0,0,0) 70%,#e23a3a 72%,#e23a3a 100%);border-radius:10px"></div>
  <p class="services-title">Services:</p>
  <ul class="services">
    <li>We deliver you empty boxes free of charge.</li>
    <li>You pack your boxes and apply our tamper seals</li>
    <li>We collect and securely store your boxes &amp; items, from $5.95 per month</li>
    <li>When you need something back, we deliver it to you within 24 hours</li>
    <li>Much more cost effective and convenient than self storage</li>
    <li>Manage your boxes online, record the contents with photos (COMING SOON)</li>
  </ul>

  <p class="contact-phone" style="left:60px;top:438px">Ph: 1300-642-118</p>
  <p class="contact-mail" style="left:76px;top:474px">Email: hello@simplycrateup.com.au</p>
  <p class="web" style="left:690px;top:446px">www.simplycrateup.com.au</p>
</section>

<section class="flyer back">
  <div class="photo" role="img" aria-label="Woman kneeling beside a letterbox-style storage unit placing a parcel inside" style="left:48px;top:38px;width:210px;height:306px;background:linear-gradient(180deg,#4a4440 0%,#d9d4c2 30%,#b9b39c 60%,#6f88b5 100%)"></div>

  <p class="how-title">How the service works</p>
  <div class="steps">
    <div class="step"><h3>We Deliver</h3><p>To your door, at your convenience<br>for FREE.</p></div>
    <div class="step"><h3>You Pack</h3><p>Take your time, pack at your own<br>pace - we give you up to a week.</p></div>
    <div class="step"><h3>We Collect &amp; Store</h3><p>When you're ready we collect<br>your filled boxes, for FREE.</p></div>
    <div class="step"><h3>We Return</h3><p>When you need something we<br>can drop it back within 24 hours</p></div>
  </div>

  <div class="brand-name" style="left:724px;top:22px;font-size:66px"><span class="mark" style="width:48px;height:48px"></span>Crate Up!</div>

  <div class="band-dark" style="top:382px"></div>
  <div class="band-blue" style="top:414px;height:97px"></div>

  <div class="store-card">
    <h2>What can I store?</h2>
    <p>There are lots of examples of what you might want to store in Crate Up boxes. These inlcuded books, clothing, documents, old toys, sentimental objects and the like. However you would want to avoid really fragile objects (glass, pottery etc). If in doubt give us a call, and always wrap it in bubble wrap</p>
  </div>

  <p class="contact-phone" style="left:60px;top:440px">Ph: 1300-642-118</p>
  <p class="contact-mail" style="left:76px;top:476px">Email: hello@simplycrateup.com.au</p>
  <p class="address">PO BOX 482 Elmwood North 3190,Melbourne</p>
  <p class="web" style="left:436px;top:466px">www.simplycrateup.com.au</p>
</section>

</body>
</html>
```